TRUCKING/TRANSPORTATION COMPANY BUSINESS CARD.

We need a business card design for our trucking company based in Tupelo, MS.
It will be a double sided design.
FRONT SIDE:
We need a good looking logo with a tagline. The tagline should match the type of business.
COMPANY NAME: RW HAULAGE LLC
BACK SIDE:
The following information should be displayed on the back of the card.
Office: 555.274.0918
Mailing: 482 W. Birch Ave.
Tupelo, MS 30917
Email: rwhaulllc@mailbox-example.net
FRONT SIDE:
BACK SIDE:
Office: 555.274.0918
Mailing: 482 W. Birch Ave.
Tupelo, MS 30917

```html
<!DOCTYPE html>
<html lang="en">
<head>
<meta charset="utf-8">
<title>RW Haulage LLC — Business Card</title>
<link rel="stylesheet" href="https://fonts.googleapis.com/css2?family=Oswald:wght@400;500;600&display=swap">
<style>
  :root {
    --stage: #1a1a1a;
    --card-dark: #1c1c1e;
    --card-light: #fbfbfb;
    --brand-blue: #1f8ab8;
    --brand-gold: #c9a22a;
    --ink: #3b3b3b;
    --muted: #8a8a8a;
  }
  * { margin: 0; padding: 0; box-sizing: border-box; }
  html, body {
    width: 1200px;
    height: 871px;
    overflow: hidden;
    background: var(--stage);
    font-family: "Oswald", "Arial Narrow", sans-serif;
  }
  .card {
    position: absolute;
    width: 640px;
    height: 366px;
    overflow: hidden;
    box-shadow: 0 12px 30px rgba(0,0,0,.55);
  }
  .card-front { left: 60px; top: 50px; background: var(--card-dark); }
  .card-back  { left: 500px; top: 455px; background: var(--card-light); }

  .card-bands { position: absolute; inset: 0; width: 100%; height: 100%; }

  .brand {
    position: absolute;
    display: flex;
    align-items: center;
    gap: 12px;
  }
  .brand-mark { width: 18px; height: 18px; background: var(--brand-gold); }
  .brand-name {
    font-weight: 600;
    letter-spacing: 2px;
    white-space: nowrap;
  }
  .card-front .brand {
    left: 0; right: 0; top: 160px;
    justify-content: center;
  }
  .card-front .brand-name { font-size: 36px; color: var(--muted); }

  .card-back .brand {
    left: 40px; top: 166px;
  }
  .card-back .brand-name { font-size: 22px; color: var(--ink); letter-spacing: 1.5px; }

  .divider {
    position: absolute;
    left: 300px; top: 60px;
    width: 3px; height: 200px;
    background: var(--brand-gold);
  }
  .contact {
    position: absolute;
    left: 324px; top: 74px;
    color: var(--ink);
  }
  .contact-name { font-size: 34px; font-weight: 600; letter-spacing: 1px; margin-bottom: 8px; }
  .contact-list { list-style: none; }
  .contact-item {
    display: flex;
    align-items: center;
    gap: 10px;
    font-size: 17px;
    font-weight: 500;
    letter-spacing: .6px;
    line-height: 30px;
    white-space: nowrap;
  }
  .contact-icon { width: 16px; height: 16px; flex: none; fill: var(--brand-blue); }
</style>
</head>
<body>

<section class="card card-front" aria-label="Card front">
  <svg class="card-bands" viewBox="0 0 640 366" aria-hidden="true">
    <polygon points="0,0 70,0 0,55" fill="var(--brand-gold)"/>
    <polygon points="70,0 180,0 0,105 0,55" fill="var(--brand-blue)"/>
    <polygon points="640,250 640,366 500,366" fill="var(--brand-gold)"/>
    <polygon points="640,290 640,330 585,366 540,366" fill="var(--card-dark)"/>
    <polygon points="640,200 640,250 500,366 420,366" fill="var(--brand-blue)"/>
  </svg>
  <div class="brand">
    <span class="brand-mark"></span>
    <span class="brand-name">RW HAULAGE LLC</span>
  </div>
</section>

<section class="card card-back" aria-label="Card back">
  <div class="brand">
    <span class="brand-mark"></span>
    <span class="brand-name">RW HAULAGE LLC</span>
  </div>
  <div class="divider"></div>
  <div class="contact">
    <p class="contact-name">Your Name</p>
    <ul class="contact-list">
      <li class="contact-item">
        <svg class="contact-icon" viewBox="0 0 16 16" aria-hidden="true"><path d="M1 6c0-2 3-3 7-3s7 1 7 3v1h-4V5.5H5V7H1z M3 8h10l1 5H2z"/></svg>
        555.274.0918
      </li>
      <li class="contact-item">
        <svg class="contact-icon" viewBox="0 0 16 16" aria-hidden="true"><path d="M8 1a5 5 0 0 0-5 5c0 4 5 9 5 9s5-5 5-9a5 5 0 0 0-5-5zm0 7a2 2 0 1 1 0-4 2 2 0 0 1 0 4z"/></svg>
        482 W. Birch Ave. Tupelo, MS 30917
      </li>
      <li class="contact-item">
        <svg class="contact-icon" viewBox="0 0 16 16" aria-hidden="true"><path d="M1 4h14v1L8 9 1 5z M1 6.5l7 4 7-4V12H1z"/></svg>
        rwhaulllc@mailbox-example.net
      </li>
    </ul>
  </div>
</section>

</body>
</html>
```